Bref créative
Corvane Oral Care Stationary
Corvane Oral Care
Professional
R. Lucien Dorvash, DDS, MAGD
2483 W Perrin Ave.
Marbeck, TX 70614
dentist@qbl.zx.com
www.corvaneoralcare.com

```html
<!DOCTYPE html>
<html lang="en">
<head>
<meta charset="utf-8">
<title>Corvane Oral Care – Stationery</title>
<link href="https://fonts.googleapis.com/css2?family=Arimo:wght@400;700&display=swap" rel="stylesheet">
<style>
  :root {
    --stage: #e9e9e9;
    --card-white: #ffffff;
    --card-dark: #3a3a3a;
    --band-dark: #1f1f1f;
    --ink: #222222;
    --teal: #2fa7a0;
    --navy: #2a3f8f;
    --accent-line: #4a5fb8;
  }
  * { box-sizing: border-box; margin: 0; padding: 0; }
  html, body { width: 1200px; height: 851px; overflow: hidden; }
  body {
    background: var(--stage);
    font-family: "Arimo", Arial, sans-serif;
    position: relative;
  }
  .card {
    position: absolute;
    border-radius: 12px;
    overflow: hidden;
    box-shadow: 0 3px 10px rgba(0,0,0,0.18);
  }
  .card--front {
    left: 377px; top: 139px; width: 453px; height: 262px;
    background: var(--card-white);
  }
  .card--back-dark {
    left: 139px; top: 410px; width: 444px; height: 269px;
    background: linear-gradient(160deg, #474747, var(--card-dark) 60%, #2e2e2e);
  }
  .card--back-light {
    left: 598px; top: 410px; width: 448px; height: 269px;
    background: linear-gradient(160deg, #ffffff, #ececec);
  }
  .brand {
    display: flex; align-items: center; gap: 10px;
    font-weight: 700; color: var(--navy);
  }
  .brand__dot {
    width: 22px; height: 22px; border-radius: 50%;
    background: var(--teal); flex: none;
  }
  .card--front .brand { position: absolute; left: 19px; top: 30px; font-size: 22px; }
  .holder {
    position: absolute; left: 86px; top: 122px;
    font-size: 12px; font-weight: 700; color: var(--ink);
  }
  .contact {
    position: absolute; left: 86px; top: 168px;
    font-size: 8.5px; line-height: 15px; color: var(--ink); font-style: normal;
  }
  .front-band {
    position: absolute; left: 0; right: 0; bottom: 0; height: 22px;
    background: var(--band-dark);
    border-top: 3px solid var(--accent-line);
    display: flex; align-items: center; justify-content: center;
  }
  .web { font-size: 9px; font-weight: 700; letter-spacing: 0.6px; }
  .front-band .web { color: #ffffff; }
  .card--back-dark .web, .card--back-light .web {
    position: absolute; left: 0; right: 0; top: 226px; text-align: center;
  }
  .card--back-dark .web { color: #d0d0d0; }
  .card--back-light .web { color: #555555; }
  .back-brand {
    position: absolute; left: 0; right: 0; top: 114px;
    justify-content: center; font-size: 24px;
  }
  .card--back-dark .back-brand { color: var(--teal); }
</style>
</head>
<body>
  <section class="card card--front">
    <div class="brand"><span class="brand__dot"></span>Corvane Oral Care</div>
    <p class="holder">R. Lucien Dorvash, DDS, MAGD</p>
    <address class="contact">
      2483 W Perrin Ave. Marbeck, TX 70614<br>
      Phone : 742-555-0142 &nbsp;|&nbsp; Fax : 742-555-0187<br>
      Email : dentist@qbl.zx.com
    </address>
    <div class="front-band"><span class="web">www.corvaneoralcare.com</span></div>
  </section>

  <section class="card card--back-dark">
    <div class="brand back-brand"><span class="brand__dot"></span>Corvane Oral Care</div>
    <p class="web">www.corvaneoralcare.com</p>
  </section>

  <section class="card card--back-light">
    <div class="brand back-brand"><span class="brand__dot"></span>Corvane Oral Care</div>
    <p class="web">www.corvaneoralcare.com</p>
  </section>
</body>
</html>
```